Wren's Hearth Support Business Card

Business card design
Font must be in Poppins Regular for Wren's Hearth Support
Safe Days Ahead font is Alex Brush

Colour must be Hex #910E2B
RGB 145-14-43
Pantone 7427 C
We want the card editable
On the front please include
Name eg Mavis Dunleavy
Position eg Clinical Care Manager
Phone number mobile 0473 856 342
Phone 08 7394 2650
Email : mavis@wrenshearthsupport.com.au
Address : Gullwing Cove, Western Australia, 6291
Website : wrenshearthsupport.com.au
Contact us today to experience the warmth, respect and personal touch of Wren's Hearth Support.

Target Market(s)

35+

Industry/Entity Type

aged care / community

Contact Information for Business Card

see project description

Requirements
Must have
• Colours, logos and fonts as detailed and uploaded

```html
<!DOCTYPE html>
<html lang="en">
<head>
<meta charset="utf-8">
<title>Wren's Hearth Support – Business Card</title>
<link href="https://fonts.googleapis.com/css2?family=Poppins:wght@400;500;700&family=Alex+Brush&display=swap" rel="stylesheet">
<style>
  :root {
    --brand: #910e2b;
    --brand-deep: #7a0b24;
    --brand-soft: #b23a55;
    --paper: #ffffff;
    --ink: #1e1e1e;
    --stage: #3a3b3d;
  }
  * { box-sizing: border-box; margin: 0; padding: 0; }
  html, body { width: 1200px; height: 939px; overflow: hidden; }
  body {
    background: var(--stage);
    font-family: "Poppins", sans-serif;
    display: flex;
    align-items: center;
    justify-content: center;
    gap: 40px;
  }
  .card {
    width: 540px;
    height: 309px;
    border-radius: 24px;
    position: relative;
    overflow: hidden;
  }

  /* Back side */
  .card--back {
    background: var(--brand);
    display: flex;
    align-items: center;
    justify-content: center;
  }
  .lockup { display: flex; align-items: center; gap: 14px; }
  .lockup__circle {
    border-radius: 50%;
    flex: none;
  }
  .lockup__text { display: flex; flex-direction: column; }
  .lockup__name {
    font-family: "Poppins", sans-serif;
    font-weight: 400;
    line-height: 1.05;
  }
  .lockup__tagline {
    font-family: "Alex Brush", cursive;
    line-height: 1;
  }
  .card--back .lockup__circle {
    width: 96px; height: 96px;
    border: 4px solid var(--brand-deep);
  }
  .card--back .lockup__name { font-size: 30px; color: var(--brand-soft); max-width: 260px; }
  .card--back .lockup__tagline { font-size: 30px; color: var(--brand-deep); margin-top: 4px; }

  /* Front side */
  .card--front {
    background: var(--paper);
    display: flex;
    align-items: center;
    padding: 0 28px 0 34px;
  }
  .card--front .lockup { width: 218px; gap: 10px; }
  .card--front .lockup__circle {
    width: 58px; height: 58px;
    border: 3px solid var(--brand);
  }
  .card--front .lockup__name { font-size: 17px; color: var(--brand); }
  .card--front .lockup__tagline { font-size: 19px; color: var(--brand); margin-top: 3px; }

  .divider {
    width: 1.5px;
    height: 196px;
    background: var(--ink);
    margin: 0 22px 0 8px;
    flex: none;
  }
  .contact { color: var(--ink); }
  .contact__name {
    font-weight: 700;
    font-size: 22px;
    color: var(--brand);
    line-height: 1.1;
  }
  .contact__role { font-size: 11.5px; margin-bottom: 12px; }
  .contact__list { list-style: none; }
  .contact__item {
    display: flex;
    align-items: center;
    gap: 7px;
    font-size: 11px;
    line-height: 1.75;
    white-space: nowrap;
  }
  .contact__icon { width: 12px; height: 12px; flex: none; fill: var(--brand); }
  .contact__address { font-size: 11px; line-height: 1.6; margin-top: 10px; padding-left: 19px; }
</style>
</head>
<body>

  <section class="card card--back" aria-label="Card back">
    <div class="lockup">
      <span class="lockup__circle"></span>
      <div class="lockup__text">
        <span class="lockup__name">Wren's Hearth Support</span>
        <span class="lockup__tagline">Safe Days Ahead</span>
      </div>
    </div>
  </section>

  <section class="card card--front" aria-label="Card front">
    <div class="lockup">
      <span class="lockup__circle"></span>
      <div class="lockup__text">
        <span class="lockup__name">Wren's Hearth Support</span>
        <span class="lockup__tagline">Safe Days Ahead</span>
      </div>
    </div>

    <span class="divider"></span>

    <div class="contact">
      <h1 class="contact__name">Mavis Dunleavy</h1>
      <p class="contact__role">Clinical Care Manager</p>
      <ul class="contact__list">
        <li class="contact__item">
          <svg class="contact__icon" viewBox="0 0 12 12"><path d="M3.5 0.5h5a1 1 0 0 1 1 1v9a1 1 0 0 1-1 1h-5a1 1 0 0 1-1-1v-9a1 1 0 0 1 1-1zm0.3 1.3v7.4h4.4V1.8zM6 9.7a0.6 0.6 0 1 0 0 1.2a0.6 0.6 0 0 0 0-1.2z"/></svg>
          0473 856 342
        </li>
        <li class="contact__item">
          <svg class="contact__icon" viewBox="0 0 12 12"><path d="M2.6 0.8l1.7 2.4-1 1.2c0.8 1.7 2.2 3.1 3.9 3.9l1.2-1 2.4 1.7-0.8 2.2C5 10.9 1 7 0.6 1.6z"/></svg>
          08 7394 2650
        </li>
        <li class="contact__item">
          <svg class="contact__icon" viewBox="0 0 12 12"><path d="M0.5 2h11v8h-11zM1.5 3v0.4l4.5 3.3 4.5-3.3V3zM1.5 4.6V9h9V4.6L6 7.9z"/></svg>
          mavis@wrenshearthsupport.com.au
        </li>
        <li class="contact__item">
          <svg class="contact__icon" viewBox="0 0 12 12"><path d="M6 0.5a5.5 5.5 0 1 0 0 11a5.5 5.5 0 0 0 0-11zm0 1c0.7 0.6 1.2 1.9 1.3 3.3H4.7C4.8 3.4 5.3 2.1 6 1.5zM3.7 4.8H1.6a4.5 4.5 0 0 1 2.8-3C3.9 2.6 3.7 3.7 3.7 4.8zm4.6 0c0-1.1-0.2-2.2-0.7-3a4.5 4.5 0 0 1 2.8 3zM1.6 5.8h2.1c0 1.1 0.2 2.2 0.7 3a4.5 4.5 0 0 1-2.8-3zm3.1 0h2.6C7.2 7.2 6.7 8.5 6 9.1 5.3 8.5 4.8 7.2 4.7 5.8zm3.6 0h2.1a4.5 4.5 0 0 1-2.8 3c0.5-0.8 0.7-1.9 0.7-3z"/></svg>
          wrenshearthsupport.com.au
        </li>
      </ul>
      <p class="contact__address">Gullwing Cove<br>Western Australia, 6291</p>
    </div>
  </section>

</body>
</html>
```